Vellora Labs - Mushroom Supplement Packaging

Our brand is called Vellora Labs. I've added a couple different logos that you can use. We are creating a line up of Mushroom Supplement products. I will add the entire line-up of products here. I've added examples of other products and packaging shape types I can purchase. Give me different options for packaging that is minimalist and clean for this brand that makes it look really well made and clean and make people want to buy.

Product 1 Lions Mane 1g
Product 2 Cordyceps 1g
Product 3 Chaga 1g
Product 4 Turkey Tail 1g
Product 5 Reishi 1g
Product 6 Maitake 1g
Product 7 Shiitake 1g

Product 8 (Mix) Lions Mane 143mg
Cordyceps 143mg
Chaga 143mg
Turkey Tail 143mg
Reishi 143mg
Maitake 143mg
Shiitake 143mg

```html
<!DOCTYPE html>
<html lang="en">
<head>
<meta charset="utf-8">
<title>Vellora Labs – Mushroom Extract Capsules</title>
<link href="https://fonts.googleapis.com/css2?family=Poppins:wght@300;400;600;700&display=swap" rel="stylesheet">
<style>
  :root {
    --page: #ffffff;
    --ink-dark: #232323;
    --ink-light: #f4f2ee;
    --chaga: #f08c2c;
    --chaga-deep: #e2801f;
    --lions-mane: #9a79bf;
    --lions-mane-deep: #8d6cb3;
    --turkey-tail: #3b96e5;
    --turkey-tail-deep: #318bd9;
  }
  * { margin: 0; padding: 0; box-sizing: border-box; }
  html, body {
    width: 1200px; height: 718px; overflow: hidden;
    background: var(--page);
    font-family: "Poppins", sans-serif;
  }
  .lineup { position: relative; width: 1200px; height: 718px; }
  .label {
    position: absolute; top: 266px; width: 304px; height: 226px;
    border-radius: 8px; overflow: hidden; color: var(--ink-light);
  }
  .label--chaga { left: 87px; background: linear-gradient(90deg, var(--chaga-deep), var(--chaga)); }
  .label--lions-mane { left: 448px; background: linear-gradient(90deg, var(--lions-mane-deep), var(--lions-mane)); }
  .label--turkey-tail { left: 809px; background: linear-gradient(90deg, var(--turkey-tail-deep), var(--turkey-tail)); }
  .label__cap { position: absolute; left: 0; top: 0; width: 304px; height: 118px; }
  .brand {
    position: absolute; top: 26px; left: 48px; display: flex; align-items: center;
  }
  .brand__name {
    font-weight: 600; font-size: 26px; line-height: 0.95; letter-spacing: 1px;
    text-transform: uppercase; color: var(--ink-light);
  }
  .brand__divider { width: 1px; height: 44px; background: var(--ink-light); opacity: .7; margin: 0 12px; }
  .brand__descriptor {
    font-weight: 300; font-size: 11px; line-height: 1.1; letter-spacing: .5px; text-transform: uppercase;
  }
  .product__art {
    position: absolute; border-radius: 44% 50% 46% 52%; background: rgba(255,255,255,.35);
  }
  .product__name {
    position: absolute; font-weight: 700; line-height: 1; letter-spacing: 0; white-space: nowrap;
  }
  .product__claim {
    position: absolute; font-weight: 600; line-height: 1.15; letter-spacing: .3px;
    text-transform: uppercase; white-space: nowrap;
  }
  .product__claim sup { font-size: 5px; }

  .label--chaga .product__art { left: 45px; top: 119px; width: 71px; height: 72px; }
  .label--chaga .product__name { left: 122px; top: 126px; font-size: 36px; }
  .label--chaga .product__claim { left: 122px; top: 164px; font-size: 7.5px; }

  .label--lions-mane .product__art { left: 24px; top: 116px; width: 44px; height: 63px; }
  .label--lions-mane .product__name { left: 77px; top: 133px; font-size: 28px; }
  .label--lions-mane .product__claim { left: 77px; top: 169px; font-size: 9.5px; }

  .label--turkey-tail .product__art { left: 23px; top: 118px; width: 53px; height: 71px; }
  .label--turkey-tail .product__name { left: 81px; top: 128px; font-size: 27.5px; }
  .label--turkey-tail .product__claim { left: 81px; top: 163px; font-size: 9.5px; }

  .supplement-type {
    position: absolute; left: 38px; top: 202px; font-weight: 400; font-size: 7px; letter-spacing: .2px;
  }
  .count { position: absolute; left: 244px; top: 194px; display: flex; align-items: center; gap: 2px; }
  .count__number { font-weight: 600; font-size: 12px; line-height: 1; }
  .count__unit { display: block; font-size: 3.5px; font-weight: 400; line-height: 1; }
</style>
</head>
<body>
<main class="lineup">

  <section class="label label--chaga">
    <svg class="label__cap" viewBox="0 0 304 118" aria-hidden="true"><path d="M0 0H304V58Q152 170 0 58Z" fill="var(--ink-dark)"/></svg>
    <div class="brand">
      <span class="brand__name">Vellora<br>Labs</span>
      <span class="brand__divider"></span>
      <span class="brand__descriptor">Mushroom<br>Extract<br>Capsules</span>
    </div>
    <div class="product__art" role="img" aria-label="Line illustration of a chaga mushroom chunk"></div>
    <h2 class="product__name">CHAGA</h2>
    <p class="product__claim">Immune support, antioxidant<br>support &amp; digestive health<sup>†</sup></p>
    <p class="supplement-type">DIETARY SUPPLEMENT</p>
    <div class="count">
      <svg width="7" height="16" viewBox="0 0 7 16" aria-hidden="true"><rect x=".6" y=".6" width="5.8" height="14.8" rx="2.9" fill="none" stroke="var(--ink-light)" stroke-width="1"/><path d="M.6 8H6.4V12.5A2.9 2.9 0 0 1 .6 12.5Z" fill="var(--ink-light)"/></svg>
      <span><span class="count__number">120</span><span class="count__unit">Capsules</span></span>
    </div>
  </section>

  <section class="label label--lions-mane">
    <svg class="label__cap" viewBox="0 0 304 118" aria-hidden="true"><path d="M0 0H304V58Q152 170 0 58Z" fill="var(--ink-dark)"/></svg>
    <div class="brand">
      <span class="brand__name">Vellora<br>Labs</span>
      <span class="brand__divider"></span>
      <span class="brand__descriptor">Mushroom<br>Extract<br>Capsules</span>
    </div>
    <div class="product__art" role="img" aria-label="Line illustration of a lion's mane mushroom"></div>
    <h2 class="product__name">LION´S MANE</h2>
    <p class="product__claim">Focus, clarity &amp; mood<sup>†</sup></p>
    <p class="supplement-type">DIETARY SUPPLEMENT</p>
    <div class="count">
      <svg width="7" height="16" viewBox="0 0 7 16" aria-hidden="true"><rect x=".6" y=".6" width="5.8" height="14.8" rx="2.9" fill="none" stroke="var(--ink-light)" stroke-width="1"/><path d="M.6 8H6.4V12.5A2.9 2.9 0 0 1 .6 12.5Z" fill="var(--ink-light)"/></svg>
      <span><span class="count__number">120</span><span class="count__unit">Capsules</span></span>
    </div>
  </section>

  <section class="label label--turkey-tail">
    <svg class="label__cap" viewBox="0 0 304 118" aria-hidden="true"><path d="M0 0H304V58Q152 170 0 58Z" fill="var(--ink-dark)"/></svg>
    <div class="brand">
      <span class="brand__name">Vellora<br>Labs</span>
      <span class="brand__divider"></span>
      <span class="brand__descriptor">Mushroom<br>Extract<br>Capsules</span>
    </div>
    <div class="product__art" role="img" aria-label="Line illustration of a turkey tail mushroom"></div>
    <h2 class="product__name">TURKEY TAIL</h2>
    <p class="product__claim">Immune support &amp; defense<sup>†</sup></p>
    <p class="supplement-type">DIETARY SUPPLEMENT</p>
    <div class="count">
      <svg width="7" height="16" viewBox="0 0 7 16" aria-hidden="true"><rect x=".6" y=".6" width="5.8" height="14.8" rx="2.9" fill="none" stroke="var(--ink-light)" stroke-width="1"/><path d="M.6 8H6.4V12.5A2.9 2.9 0 0 1 .6 12.5Z" fill="var(--ink-light)"/></svg>
      <span><span class="count__number">120</span><span class="count__unit">Capsules</span></span>
    </div>
  </section>

</main>
</body>
</html>
```